Karateverein Info Plakat
Zielgruppe
Wir sind ein recht junger Karateverein, der Hayabusa Budo Rindach e.V. Zielgruppe sollen hauptsächlich Familien sein, die für Ihr Kind eine Sportart suchen.
Aufgabenstellung
Es soll sich um ein Info Plakat handeln, das wir relativ groß drucken möchten (70cm x 100 cm ) in Hochformat. Grundfarbe sollte in rot gehalten sein. Folgende Infos sollten enthalten sein:
Unser Training fördert:
• körperliche Fitness und Koordination
• Selbstdisziplin und Selbstwertgefühl
• Selbstbewusstsein und Selbstbehauptung
• Selbstverteidigung
• Spaß und Gemeinschaft
In unserem Verein erwartet Dich:
• Kindertraining (ab drei Jahren), Jugendtraining und Erwachsenentraining
• für Anfänger, Fortgeschrittene und Quereinsteiger
• für Breitensportler:innen jeden Alterss und Leistungsgruppen
• Qualifiziertes Trainerteam mit langjähriger Erfahrung und Erfolgsnachweisen
• ein Sport für die ganze Familie
• ein aktives, gemeinschaftliches Vereinsleben
• Training findet auch in den Schulferien statt
• Monatlich kündbare flexible Mitgliedschaft
• Verein ist Mitglied im Nationalen Kampfkunstbund
• Probetraining ohne Anmeldung möglich

```html
<!DOCTYPE html>
<html lang="de">
<head>
<meta charset="utf-8">
<title>Hayabusa Budo Rindach e.V. – Info Plakat</title>
<link href="https://fonts.googleapis.com/css2?family=Source+Sans+3:wght@400;700&display=swap" rel="stylesheet">
<style>
  :root {
    --paper: #ffffff;
    --poster-red: #e3271e;
    --shadow-red: #cc251c;
    --text-white: #ffffff;
    --ink: #1a1a1a;
    --gi-light: #eeeae8;
    --gi-shade: #c9c2c0;
    --mascot-teal: #6fa9b4;
    --mascot-deep: #3f6f7c;
  }
  * { margin: 0; padding: 0; box-sizing: border-box; }
  html, body { width: 840px; height: 1200px; overflow: hidden; background: var(--paper); }
  body { position: relative; font-family: "Source Sans 3", "Myriad Pro", sans-serif; }

  .poster {
    position: absolute; left: 28px; top: 40px; width: 787px; height: 1123px;
    background: var(--poster-red); overflow: hidden;
  }
  .training-photo, .background-figure, .mascot { position: absolute; }
  .training-photo { left: 0; top: 0; width: 787px; height: 480px; }
  .background-figure { left: 210px; top: 480px; width: 577px; height: 600px; }
  .mascot { left: 536px; top: 826px; width: 251px; height: 260px; }

  .club-badge {
    position: absolute; left: 38px; top: 36px; width: 268px; height: 268px;
    border-radius: 50%; background: var(--paper); border: 4px solid var(--ink);
    display: flex; align-items: center; justify-content: center; text-align: center;
  }
  .club-name {
    font-weight: 700; font-size: 25px; line-height: 1.15; color: var(--ink); padding: 0 30px;
  }

  .headline {
    position: absolute; left: 61px; top: 352px;
    color: var(--text-white); font-weight: 700; font-size: 58px; line-height: 58px;
  }
  .content { position: absolute; left: 61px; color: var(--text-white); }
  .benefits { top: 483px; }
  .offers { top: 684px; }
  .section-title { font-weight: 700; font-size: 28px; line-height: 34px; }
  .bullet-list { list-style: none; font-size: 23px; line-height: 28px; }
  .bullet-list li { position: relative; padding-left: 12px; }
  .bullet-list li::before {
    content: "•"; position: absolute; left: 0; top: 0; font-size: 14px;
  }
</style>
</head>
<body>
  <main class="poster">
    <svg class="training-photo" viewBox="0 0 787 480" role="img" aria-label="Foto: Kinder in weißen Karateanzügen mit bunten Gürteln knien in einer Reihe">
      <defs>
        <linearGradient id="giTone" x1="0" y1="0" x2="1" y2="1">
          <stop offset="0" stop-color="var(--gi-shade)"/>
          <stop offset="0.5" stop-color="var(--gi-light)"/>
          <stop offset="1" stop-color="var(--gi-shade)"/>
        </linearGradient>
      </defs>
      <path d="M80 0 H787 V480 L600 475 C560 450 520 430 470 400 C440 370 420 340 380 300 C360 280 330 270 300 260 L60 220 L40 140 Z" fill="url(#giTone)"/>
    </svg>

    <svg class="background-figure" viewBox="0 0 577 600" role="img" aria-label="Dezente dunkelrote Hintergrundgrafik eines Karatekas">
      <defs>
        <radialGradient id="figureTone" cx="0.6" cy="0.45" r="0.55">
          <stop offset="0" stop-color="var(--shadow-red)"/>
          <stop offset="1" stop-color="var(--poster-red)"/>
        </radialGradient>
      </defs>
      <rect x="0" y="0" width="577" height="600" fill="url(#figureTone)"/>
    </svg>

    <svg class="mascot" viewBox="0 0 251 260" role="img" aria-label="Illustration: Drachen-Maskottchen im Karateanzug">
      <defs>
        <radialGradient id="mascotTone" cx="0.5" cy="0.45" r="0.55">
          <stop offset="0" stop-color="var(--mascot-teal)"/>
          <stop offset="1" stop-color="var(--mascot-deep)"/>
        </radialGradient>
      </defs>
      <ellipse cx="135" cy="135" rx="112" ry="120" fill="url(#mascotTone)"/>
    </svg>

    <div class="club-badge">
      <span class="club-name">Hayabusa Budo Rindach e.V.</span>
    </div>

    <h1 class="headline">Sport für die<br>ganze Familie</h1>

    <section class="content benefits">
      <h2 class="section-title">Unser Training fördert:</h2>
      <ul class="bullet-list">
        <li>körperliche Fitness und Koordination</li>
        <li>Selbstdisziplin und Selbstwertgefühl</li>
        <li>Selbstbewusstsein und Selbstbehauptung</li>
        <li>Selbstverteidigung</li>
        <li>Spaß und Gemeinschaft</li>
      </ul>
    </section>

    <section class="content offers">
      <h2 class="section-title">In unserem Verein erwartet Dich:</h2>
      <ul class="bullet-list">
        <li>Kindertraining (ab drei Jahren), Jugend- und Erwachsenentraining</li>
        <li>für Anfänger, Fortgeschrittene und Quereinsteiger</li>
        <li>für Breitensportler:innen jeden Alterss und Leistungsgruppen</li>
        <li>Qualifiziertes Trainerteam mit langjähriger Erfahrung<br>und Erfolgsnachweisen</li>
        <li>ein Sport für die ganze Familie</li>
        <li>ein aktives, gemeinschaftliches Vereinsleben</li>
        <li>Training findet auch in den Schulferien statt</li>
        <li>Monatlich kündbare flexible Mitgliedschaft</li>
        <li>Verein ist Mitglied im Nationalen Kampfkunstbund</li>
        <li>Probetraining ohne Anmeldung möglich</li>
      </ul>
    </section>
  </main>
</body>
</html>
```